Pizza Coupon App Design Project

*******This project will have a guaranteed payout once I see that there is quality work being designed*********

I require the design (no coding) of 4 vertical screens (the screen will not change for horizontal orientation) for iPhone and Android. The highest res should be used so it can be scaled for older generation phones.

The mobile app will be used to access pizza coupons.

I do not have a specific style or look that I am going for, although I do not want a childish design (e.g. comic sans). The main requirements are for it to be very easy for users to understand and navigate and to be clean and professional.

I am happy if you only produce a design of the main and store selection screens to which I will give feedback before continuing to design the remaining screens.

The selected artist must be flexible in adapting the final design slightly after the contest is completed, during the app development process (maybe a few small modifications over a month or so).
Please do not include any copyrighted images in your deliverables. I must be the sole owner of the graphics once I have paid for them.

I have included attachments which show the process flow and the screen requirements so that will give you the detail you need to design them. I have also included the logo to assist you in your design., *******This project is now guaranteed *********

I have included attachments which show the process flow and the screen requirements so that will give you the detail you need to design them. I have also included the logo to assist you in your design., *******This project will have a guaranteed payout once I see that there is quality work being designed*********

I have included attachments which show the process flow and the screen requirements so that will give you the detail you need to design them. I have also included the logo to assist you in your design.

Reason: Still looking for the perfect design! ******Project is now guaranteed******

******Project is now guaranteed******

Reason: Starting to get some great designs, we are getting much closer! Keep it up.

students and 18-30 year olds - People who want cheap meals and people who order pizza online., students and 18-30 year olds - People who want cheap meals and people who order pizza online., students and 18-30 year olds - People who want cheap meals and people who order pizza online.

Store

• Must have requirements are listed in the attached documents., Must have requirements are listed in the attached documents., Must have requirements are listed in the attached documents.

```html
<!DOCTYPE html>
<html lang="en">
<head>
<meta charset="utf-8">
<title>Pizza Coupons – Store List</title>
<link href="https://fonts.googleapis.com/css2?family=Arimo:wght@400;700&family=Oswald:wght@500&family=Roboto+Condensed:wght@700&family=Open+Sans:wght@400&display=swap" rel="stylesheet">
<style>
  :root{
    --page:#c9ab84;
    --status:#000;
    --banner-hi:#d8682a;
    --banner-lo:#7a1f0c;
    --banner-text:#f1cf5c;
    --toolbar-hi:#8a7560;
    --toolbar-lo:#4b3a2b;
    --field:#ffffff;
    --caret:#1a5bd6;
    --content:#4a3425;
    --row-light-hi:#f3e7c9;
    --row-light-lo:#d9c7a0;
    --row-dark-hi:#8c7764;
    --row-dark-lo:#6a5544;
    --title-light:#ffffff;
    --sub-light:#5a4a38;
    --sub-dark:#f2e8dc;
    --pill:#a39584;
    --pill-dark:#5b4a3b;
    --tab-hi:#6d5845;
    --tab-lo:#3d2c1f;
    --tab-text:#ffffff;
  }
  html,body{margin:0;width:1200px;height:971px;overflow:hidden;background:var(--page);}
  .stage{position:relative;width:1200px;height:971px;}
  .screen{position:absolute;top:204px;width:352px;height:528px;background:var(--content);overflow:hidden;font-family:"Arimo",Arial,sans-serif;}
  .screen--light{left:160px;}
  .screen--dark{left:700px;}
  .status{height:20px;background:var(--status);color:#fff;font-size:14px;font-weight:700;display:flex;align-items:center;justify-content:space-between;padding:0 6px;box-sizing:border-box;}
  .status__carrier{display:flex;align-items:center;gap:4px;font-size:13px;}
  .status__time{position:absolute;left:0;right:0;text-align:center;font-size:14px;}
  .banner{height:68px;background:radial-gradient(ellipse at center,var(--banner-hi) 0%,#b1401a 55%,var(--banner-lo) 100%);display:flex;align-items:center;justify-content:center;gap:12px;}
  .banner__title{font-family:"Oswald",Arial,sans-serif;font-weight:500;font-size:36px;color:var(--banner-text);letter-spacing:1px;}
  .toolbar{height:48px;background:linear-gradient(var(--toolbar-hi),var(--toolbar-lo));position:relative;}
  .search{position:absolute;left:40px;top:9px;width:252px;height:29px;border-radius:15px;background:var(--field);box-shadow:inset 0 1px 3px rgba(0,0,0,.5);}
  .search svg{position:absolute;left:10px;top:7px;}
  .search__caret{position:absolute;left:33px;top:6px;width:3px;height:18px;background:var(--caret);}
  .add{position:absolute;left:304px;top:9px;width:37px;height:30px;border-radius:5px;background:linear-gradient(#6f5e50,#3e3128);box-shadow:0 0 0 1px rgba(0,0,0,.4);}
  .add svg{position:absolute;left:10px;top:7px;}
  .store{position:relative;height:53px;border-bottom:1px solid rgba(0,0,0,.35);}
  .screen--light .store{background:linear-gradient(var(--row-light-hi),var(--row-light-lo));}
  .screen--dark .store{background:linear-gradient(var(--row-dark-hi),var(--row-dark-lo));}
  .store__icon{position:absolute;left:12px;top:11px;width:20px;height:30px;border-radius:3px;background:linear-gradient(#e0b25a,#b33a1e);}
  .store__name{position:absolute;left:45px;top:9px;font-size:15px;font-weight:700;color:var(--title-light);text-shadow:0 1px 1px rgba(0,0,0,.35);}
  .store__address{position:absolute;left:45px;top:29px;font-family:"Open Sans",Arial,sans-serif;font-size:12.5px;}
  .screen--light .store__address{color:var(--sub-light);}
  .screen--dark .store__address{color:var(--sub-dark);}
  .store__count{position:absolute;left:280px;top:14px;width:40px;height:24px;border-radius:12px;font-size:12px;line-height:24px;text-align:center;}
  .screen--light .store__count{background:var(--pill);color:#e9e0d3;}
  .screen--dark .store__count{background:var(--pill-dark);color:#d8cbbd;}
  .store__chevron{position:absolute;left:333px;top:18px;}
  .tabbar{position:absolute;left:0;bottom:0;width:352px;height:52px;background:linear-gradient(var(--tab-hi),var(--tab-lo));}
  .tabbar__promo{position:absolute;left:120px;top:4px;width:122px;height:48px;border-radius:24px 24px 0 0;background:radial-gradient(ellipse at center,#a86a3f 0%,#7a4d30 60%,rgba(90,60,40,0) 100%);}
  .tab{position:absolute;top:4px;width:90px;text-align:center;color:var(--tab-text);font-family:"Roboto Condensed",Arial,sans-serif;font-weight:700;font-size:11px;}
  .tab svg{display:block;margin:0 auto 1px;}
  .tab--find{left:13px;}
  .tab--submit{left:248px;}
</style>
</head>
<body>
<main class="stage">

  <section class="screen screen--light">
    <div class="status">
      <span class="status__carrier">
        <svg width="18" height="9"><rect x="0" y="6" width="3" height="3" fill="#fff"/><rect x="4" y="4" width="3" height="5" fill="#fff"/><rect x="8" y="2" width="3" height="7" fill="#fff"/><rect x="12" y="0" width="3" height="9" fill="#fff"/></svg>Nordcell
      </span>
      <span class="status__time">9:42 AM</span>
      <svg width="22" height="10"><rect x="0.5" y="0.5" width="18" height="9" rx="1.5" fill="none" stroke="#fff"/><rect x="2" y="2" width="11" height="6" fill="#fff"/><rect x="19" y="3" width="2" height="4" fill="#fff"/></svg>
    </div>
    <header class="banner">
      <svg width="50" height="22"><rect x="0" y="3" width="50" height="3" fill="var(--banner-text)"/><rect x="12" y="10" width="38" height="3" fill="var(--banner-text)"/><rect x="22" y="17" width="28" height="3" fill="var(--banner-text)"/></svg>
      <span class="banner__title">ADVERTISING</span>
      <svg width="50" height="22"><rect x="0" y="3" width="50" height="3" fill="var(--banner-text)"/><rect x="0" y="10" width="38" height="3" fill="var(--banner-text)"/><rect x="0" y="17" width="28" height="3" fill="var(--banner-text)"/></svg>
    </header>
    <div class="toolbar">
      <div class="search">
        <svg width="16" height="16"><circle cx="6.5" cy="6.5" r="5" fill="none" stroke="#999" stroke-width="2"/><line x1="10" y1="10" x2="14.5" y2="14.5" stroke="#999" stroke-width="2.4"/></svg>
        <span class="search__caret"></span>
      </div>
      <div class="add"><svg width="17" height="17"><rect x="7" y="0" width="3" height="17" fill="#fff"/><rect x="0" y="7" width="17" height="3" fill="#fff"/></svg></div>
    </div>
    <div class="store">
      <span class="store__icon" role="img" aria-label="Pizza slice icon"></span>
      <span class="store__name">Store name</span>
      <span class="store__address">Address, World Avenue 123</span>
      <span class="store__count">5</span>
      <svg class="store__chevron" width="10" height="16"><polyline points="2,2 8,8 2,14" fill="none" stroke="#5a4a3a" stroke-width="3"/></svg>
    </div>
    <div class="store">
      <span class="store__icon" role="img" aria-label="Pizza slice icon"></span>
      <span class="store__name">Store name</span>
      <span class="store__address">Address, World Avenue 123</span>
      <span class="store__count">5</span>
      <svg class="store__chevron" width="10" height="16"><polyline points="2,2 8,8 2,14" fill="none" stroke="#5a4a3a" stroke-width="3"/></svg>
    </div>
    <nav class="tabbar">
      <span class="tabbar__promo" role="img" aria-label="Pizza with percent-off tag"></span>
      <span class="tab tab--find">
        <svg width="32" height="30"><circle cx="13" cy="12" r="9" fill="none" stroke="#d8cfc6" stroke-width="3"/><line x1="20" y1="19" x2="28" y2="27" stroke="#d8cfc6" stroke-width="4"/></svg>Find coupons</span>
      <span class="tab tab--submit">
        <svg width="32" height="30"><polyline points="18,9 18,3 6,3 6,27 18,27 18,21" fill="none" stroke="#d8cfc6" stroke-width="3"/><polyline points="12,15 28,15" stroke="#d8cfc6" stroke-width="3"/><polyline points="23,10 28,15 23,20" fill="none" stroke="#d8cfc6" stroke-width="3"/></svg>Submit coupons</span>
    </nav>
  </section>

  <section class="screen screen--dark">
    <div class="status">
      <span class="status__carrier">
        <svg width="18" height="9"><rect x="0" y="6" width="3" height="3" fill="#fff"/><rect x="4" y="4" width="3" height="5" fill="#fff"/><rect x="8" y="2" width="3" height="7" fill="#fff"/><rect x="12" y="0" width="3" height="9" fill="#fff"/></svg>Nordcell
      </span>
      <span class="status__time">9:42 AM</span>
      <svg width="22" height="10"><rect x="0.5" y="0.5" width="18" height="9" rx="1.5" fill="none" stroke="#fff"/><rect x="2" y="2" width="11" height="6" fill="#fff"/><rect x="19" y="3" width="2" height="4" fill="#fff"/></svg>
    </div>
    <header class="banner">
      <svg width="50" height="22"><rect x="0" y="3" width="50" height="3" fill="var(--banner-text)"/><rect x="12" y="10" width="38" height="3" fill="var(--banner-text)"/><rect x="22" y="17" width="28" height="3" fill="var(--banner-text)"/></svg>
      <span class="banner__title">ADVERTISING</span>
      <svg width="50" height="22"><rect x="0" y="3" width="50" height="3" fill="var(--banner-text)"/><rect x="0" y="10" width="38" height="3" fill="var(--banner-text)"/><rect x="0" y="17" width="28" height="3" fill="var(--banner-text)"/></svg>
    </header>
    <div class="toolbar">
      <div class="search">
        <svg width="16" height="16"><circle cx="6.5" cy="6.5" r="5" fill="none" stroke="#999" stroke-width="2"/><line x1="10" y1="10" x2="14.5" y2="14.5" stroke="#999" stroke-width="2.4"/></svg>
        <span class="search__caret"></span>
      </div>
      <div class="add"><svg width="17" height="17"><rect x="7" y="0" width="3" height="17" fill="#fff"/><rect x="0" y="7" width="17" height="3" fill="#fff"/></svg></div>
    </div>
    <div class="store">
      <span class="store__icon" role="img" aria-label="Pizza slice icon"></span>
      <span class="store__name">Store name</span>
      <span class="store__address">Address, World Avenue 123</span>
      <span class="store__count">5</span>
      <svg class="store__chevron" width="10" height="16"><polyline points="2,2 8,8 2,14" fill="none" stroke="#4a3a2c" stroke-width="3"/></svg>
    </div>
    <div class="store">
      <span class="store__icon" role="img" aria-label="Pizza slice icon"></span>
      <span class="store__name">Store name</span>
      <span class="store__address">Address, World Avenue 123</span>
      <span class="store__count">5</span>
      <svg class="store__chevron" width="10" height="16"><polyline points="2,2 8,8 2,14" fill="none" stroke="#4a3a2c" stroke-width="3"/></svg>
    </div>
    <div class="store">
      <span class="store__icon" role="img" aria-label="Pizza slice icon"></span>
      <span class="store__name">Store name</span>
      <span class="store__address">Address, World Avenue 123</span>
      <span class="store__count">5</span>
      <svg class="store__chevron" width="10" height="16"><polyline points="2,2 8,8 2,14" fill="none" stroke="#4a3a2c" stroke-width="3"/></svg>
    </div>
    <nav class="tabbar">
      <span class="tabbar__promo" role="img" aria-label="Pizza with percent-off tag"></span>
      <span class="tab tab--find">
        <svg width="32" height="30"><circle cx="13" cy="12" r="9" fill="none" stroke="#d8cfc6" stroke-width="3"/><line x1="20" y1="19" x2="28" y2="27" stroke="#d8cfc6" stroke-width="4"/></svg>Find coupons</span>
      <span class="tab tab--submit">
        <svg width="32" height="30"><polyline points="18,9 18,3 6,3 6,27 18,27 18,21" fill="none" stroke="#d8cfc6" stroke-width="3"/><polyline points="12,15 28,15" stroke="#d8cfc6" stroke-width="3"/><polyline points="23,10 28,15 23,20" fill="none" stroke="#d8cfc6" stroke-width="3"/></svg>Submit coupons</span>
    </nav>
  </section>

</main>
</body>
</html>
```